Business Cards for IT Consulting Company (Managed Service Provider)

I am looking to have some business cards printed and would like some designs. We are an IT Consulting company based in Vancouver BC. I would like a nice clean and modern look to the cards. I have uploaded all the versions of my logo so parts can be used as needed. Here is a snippit from our website homepage:

Kelbrook Systems Ltd. is an IT Solutions Partner located in Vancouver BC, Canada. We offer IT solutions and support to customers in the greater Vancouver Area. With expertise in Microsoft platforms, as well as Linux and Mac OSX and over 12 years experience in the IT industry, Kelbrook Systems is dedicated to offering our clients top quality service and products. We take pride in the solutions we offer our customers. The greatest compliment a client can give us is to recommend our services.

Kelbrook Systems Ltd. offers a wide range of IT services from onsite service to remote support and managed service solutions. This allows clients to choose the support path that best suits their company’s needs. Supporting many different sized companies from small to enterprise level over the past 12 years Kelbrook Systems has the experience and expertise needed to ensure things run smoothly. Allowing our clients to focus on doing business.

Revolutionizing the way IT services are delivered.

Kelbrook Systems is dedicated to providing our clients with IT solutions that work and grow with them for years to come. This philosophy helps save money in the long run instead of replacing equipment constantly. Far too often IT solutions are not well thought out and while possibly solving the problem at hand, require replacement due to growth or quality within a very short time frame. Kelbrook Systems takes pride in providing solutions that will last and be able to accommodate growth without the need for replacement.

Industry/Entity Type

Information Technology

Contact Information for Business Card

Kelbrook Systems Ltd.
(Employee Name)
Eml: (Employees Email Address)
Web: kelbrook.me
Ph: 604-555-0142

Font styles to use
Serif
Sans Serif

Requirements
Must have
• The Company logo and company colors.
Nice to have
• - Our tag line: "Revolutionizing IT Services" or "Revolutionizing the way IT services are delivered."
• - Also I really like the idea of nature and technology together blending which is sort of where my logo came from so integrating that somehow onto the business cards would be great.

```html
<!DOCTYPE html>
<html lang="en">
<head>
<meta charset="utf-8">
<title>Kelbrook Systems Ltd. – Business Card</title>
<link href="https://fonts.googleapis.com/css2?family=Open+Sans:wght@400;600;700&display=swap" rel="stylesheet">
<style>
  :root {
    --backdrop: #c9c9c9;
    --brand-blue: #2ca8e0;
    --accent-blue: #2a9fd8;
    --pattern-blue: #d6e9f6;
    --paper: #ffffff;
  }
  * { box-sizing: border-box; margin: 0; padding: 0; }
  html, body {
    width: 1200px; height: 1200px; overflow: hidden;
    background: var(--backdrop);
    font-family: "Open Sans", Arial, sans-serif;
  }
  .sheet {
    width: 1200px; height: 1200px;
    display: flex; flex-direction: column; align-items: center; justify-content: center;
    gap: 60px;
  }
  .card {
    position: relative; width: 900px; height: 514px; overflow: hidden;
    box-shadow: 0 6px 18px rgba(0,0,0,.18);
  }

  /* Front */
  .card--front { background: var(--brand-blue); }
  .rule { position: absolute; height: 6px; background: var(--paper); }
  .rule--upper { left: 0; top: 120px; width: 300px; }
  .rule--lower { left: 720px; top: 254px; width: 180px; }
  .name-plate {
    position: absolute; left: 300px; top: 120px; width: 420px; height: 140px;
    background: var(--paper);
    display: flex; align-items: center; justify-content: center; gap: 18px;
  }
  .name-plate__mark { width: 34px; height: 34px; border-radius: 50%; background: var(--brand-blue); }
  .name-plate__name { color: var(--brand-blue); font-weight: 700; font-size: 42px; letter-spacing: -0.5px; }
  .tagline {
    position: absolute; left: 60px; bottom: 60px;
    color: var(--paper); font-weight: 700; font-size: 17px; letter-spacing: 6px;
  }

  /* Back */
  .card--back { background: var(--paper); }
  .pattern-area {
    position: absolute; left: 0; top: 0; width: 440px; height: 514px;
    background: linear-gradient(135deg, var(--pattern-blue), #eef6fb);
  }
  .contact {
    position: absolute; right: 60px; top: 80px; text-align: right; color: var(--accent-blue);
  }
  .contact__company { font-size: 30px; font-weight: 400; }
  .contact__company strong { font-weight: 700; }
  .contact__person { font-size: 40px; font-weight: 700; margin-top: 6px; }
  .contact__person span { border-bottom: 3px solid var(--accent-blue); padding-bottom: 2px; }
  .contact__list { list-style: none; margin-top: 62px; font-size: 24px; line-height: 1.45; }
  .contact__list li { display: flex; align-items: center; justify-content: flex-end; gap: 14px; }
  .contact__list svg { width: 24px; height: 24px; fill: var(--accent-blue); flex: none; }
</style>
</head>
<body>
<main class="sheet">
  <section class="card card--front" aria-label="Card front">
    <div class="rule rule--upper"></div>
    <div class="name-plate">
      <span class="name-plate__mark"></span>
      <span class="name-plate__name">Kelbrook Systems</span>
    </div>
    <div class="rule rule--lower"></div>
    <p class="tagline">Revolutionizing IT Services</p>
  </section>

  <section class="card card--back" aria-label="Card back">
    <div class="pattern-area" role="img" aria-label="Large light-blue brand pattern decoration"></div>
    <div class="contact">
      <p class="contact__company"><strong>Kelbrook</strong> Systems Ltd.</p>
      <p class="contact__person">(Employee <span>Name)</span></p>
      <ul class="contact__list">
        <li>604-555-0142
          <svg viewBox="0 0 24 24" aria-hidden="true"><path d="M3 8c0-3 4-4 9-4s9 1 9 4v2h-5V8H8v2H3zM6 12h12l2 8H4z"/></svg>
        </li>
        <li>kelbrook.me
          <svg viewBox="0 0 24 24" aria-hidden="true"><path d="M12 2a10 10 0 100 20 10 10 0 000-20zm0 2c1 0 2.4 2 2.9 5H9.1C9.6 6 11 4 12 4zM4.3 11h4.6a18 18 0 000 2H4.3a8 8 0 010-2zm6.6 0h2.2a16 16 0 010 2h-2.2a16 16 0 010-2zm4.2 0h4.6a8 8 0 010 2h-4.6a18 18 0 000-2zM9.1 15h5.8c-.5 3-1.9 5-2.9 5s-2.4-2-2.9-5z"/></svg>
        </li>
        <li>(Employees Email Address)
          <svg viewBox="0 0 24 24" aria-hidden="true"><path d="M2 5h20v14H2zm2 2v.4l8 5.6 8-5.6V7z"/></svg>
        </li>
      </ul>
    </div>
  </section>
</main>
</body>
</html>
```